menu tolbeno

nesecitamos nuestro menu para restaurante mexicano lo qu ebuscamos es un menu moderno pero ala vez elegante de preferencia fondo negro o cafe y letras blancas o letras visibles con fotos

Target Market(s)

personas de todas edades

Industry/Entity Type

Mexican Restaurant

Font styles to use
Sans Serif

Colors
000000
fbfbfb
ec1f27
fbe7d2

Requirements
Must have
• elegancia, moderno presencia
Nice to have
• portada de menu logotipo con fondo moderno

```html
<!DOCTYPE html>
<html lang="en">
<head>
<meta charset="UTF-8">
<title>Tolbeno Menu</title>
<link rel="stylesheet" href="https://fonts.googleapis.com/css2?family=Cinzel:wght@400;600;700&family=Lato:wght@400&display=swap">
<style>
:root{
  --ink:#161616;
  --panel:#1e1c1c;
  --white:#fbfbfb;
  --cream:#fbe7d2;
  --canvas:#efefef;
  --accent:#d9822b;
}
*{margin:0;padding:0;box-sizing:border-box}
html,body{width:1200px;height:1200px;overflow:hidden;background:var(--canvas)}
.menu-page{position:absolute;left:151px;top:19px;width:898px;height:1162px;overflow:hidden;
  font-family:"Cinzel",serif;color:var(--ink)}
.page-backdrop{position:absolute;inset:0;
  background:linear-gradient(180deg,#f3dcc4 0%,#f2d9c6 40%,#e7dcd6 70%,#dcd6d4 100%)}
.shapes{position:absolute;inset:0}
.section-title{position:absolute;font-size:27px;line-height:1;font-weight:600;letter-spacing:.5px}
.item-name{position:absolute;font-size:18px;line-height:1;letter-spacing:.6px;white-space:nowrap}
.item-desc{position:absolute;font-size:10px;line-height:13px;letter-spacing:.2px;text-transform:uppercase}
.price{position:absolute;font-size:17px;line-height:1;text-align:right;width:70px}
.on-dark{color:var(--white)}
.brand-badge{position:absolute;left:751px;top:181px;width:112px;height:112px;border-radius:50%;
  background:var(--white);display:flex;align-items:center;justify-content:center}
.brand-name{font-family:"Cinzel",serif;font-size:17px;font-weight:400;color:var(--accent);letter-spacing:1px}
.extras{position:absolute;left:138px;top:1046px;width:618px;text-align:center;color:var(--white)}
.extras-fee{font-size:12px;margin-top:9px;letter-spacing:.5px;text-transform:uppercase}
.extras-list{font-size:14.5px;line-height:18px;margin-top:6px;letter-spacing:.4px;text-transform:uppercase}
.extras-notice{font-family:"Lato",sans-serif;font-size:10px;line-height:13px;margin-top:3px}
</style>
</head>
<body>
<main class="menu-page">
  <div class="page-backdrop" role="img" aria-label="Faded photo of a restaurant table with plated Mexican dishes"></div>
  <svg class="shapes" width="898" height="1162" viewBox="0 0 898 1162">
    <defs>
      <linearGradient id="moleTone" x1="0" y1="0" x2="1" y2="1">
        <stop offset="0" stop-color="#5a3a24"/>
        <stop offset=".5" stop-color="#3a2418"/>
        <stop offset="1" stop-color="#9a8f88"/>
      </linearGradient>
    </defs>
    <path role="img" aria-label="Photo of enchiladas covered in mole sauce with cream and cheese"
      d="M0 0 H898 V292 Q898 317 870 317 H500 Q470 317 466 287 L457 186 Q453 156 425 156 H0 Z"
      fill="url(#moleTone)" stroke="#000" stroke-width="8"/>
    <rect x="-10" y="206" width="20" height="300" rx="10" fill="#000"/>
    <rect x="890" y="525" width="20" height="280" rx="10" fill="#1a1a1a"/>
    <line x1="446" y1="203" x2="446" y2="545" stroke="#555" stroke-width="1"/>
    <path d="M0 518 H418 Q450 518 450 550 V979 Q450 1011 418 1011 H0 Z" fill="var(--panel)" opacity=".95"/>
    <rect role="img" aria-label="Photo of shredded chicken with guacamole, sour cream and tomato" x="472" y="850" width="181" height="159" rx="20" fill="#a9b07a" stroke="#333" stroke-width="2"/>
    <rect role="img" aria-label="Photo of steak with pico de gallo and guacamole" x="686" y="850" width="181" height="159" rx="20" fill="#7a5238" stroke="#333" stroke-width="2"/>
    <path d="M138 1076 Q138 1046 168 1046 H726 Q756 1046 756 1076 V1160 H138 Z" fill="var(--panel)"/>
    <rect x="0" y="1153" width="898" height="9" fill="#000"/>
  </svg>

  <div class="brand-badge"><span class="brand-name">TOLBENO</span></div>

  <!-- Seafood -->
  <h2 class="section-title" style="left:35px;top:220px">Seafood</h2>
  <div class="item-name" style="left:32px;top:276px">Camarones Tolbeno</div>
  <div class="price" style="left:354px;top:279px">$13.99</div>
  <p class="item-desc" style="left:32px;top:300px;width:360px">Grilled shrimp and bell pepper in a special cheese sauce served with rice and tossed salad</p>
  <div class="item-name" style="left:32px;top:340px">Camarones a la Diabla</div>
  <div class="price" style="left:354px;top:341px">$13.99</div>
  <p class="item-desc" style="left:32px;top:360px;width:340px">Shrimp cooked with diabla sauce served with rice and tossed salad</p>
  <div class="item-name" style="left:32px;top:400px">Coctel de Camarone</div>
  <div class="price" style="left:354px;top:403px">$13.99</div>
  <div class="item-desc" style="left:32px;top:429px;font-size:14px;line-height:18px">-Small<br>-Large</div>
  <div class="price" style="left:354px;top:427px;line-height:23px">$7.50<br>$12.75</div>

  <!-- Tacos -->
  <h2 class="section-title on-dark" style="left:26px;top:535px">Tacos</h2>
  <div class="item-name on-dark" style="left:23px;top:577px">Tacos Americanos</div>
  <div class="price on-dark" style="left:345px;top:578px">$7.25</div>
  <p class="item-desc on-dark" style="left:23px;top:600px;width:340px">Three tacos with ground beef or shredded chicken served with lettuce, cheese and tomatoes. Served in hard or soft tortillas</p>
  <div class="item-name on-dark" style="left:23px;top:653px">Tacos de Carne Asada</div>
  <div class="price on-dark" style="left:353px;top:654px">$10.99</div>
  <p class="item-desc on-dark" style="left:27px;top:673px;width:345px">Fo7ur steak tacos served in soft corn tortillas, with pico de gallo and green sauce.</p>
  <div class="item-name on-dark" style="left:23px;top:713px">Tacos de Carnitas</div>
  <div class="price on-dark" style="left:353px;top:732px">$10.99</div>
  <p class="item-desc on-dark" style="left:27px;top:734px;width:310px">Four pork carnitas tacos served in soft corn tortillas, with pico de gallo and green sauce.</p>
  <div class="item-name on-dark" style="left:24px;top:781px">Tacos de Pescado</div>
  <div class="price on-dark" style="left:353px;top:782px">$11.50</div>
  <p class="item-desc on-dark" style="left:24px;top:804px;width:345px">Four fish tacos served in soft corn tortillas, with pico de gallo and green sauce.</p>
  <div class="item-name on-dark" style="left:24px;top:847px">Tacos de Pastor</div>
  <div class="price on-dark" style="left:353px;top:848px">$11.50</div>
  <p class="item-desc on-dark" style="left:27px;top:868px;width:320px">Four marinete pork tacos coocked with pine appleserved in soft corn tortillas with cilantro, onions and sauce green</p>
  <div class="item-name on-dark" style="left:24px;top:916px">Taquitos Mexicanos</div>
  <div class="price on-dark" style="left:345px;top:915px">$9.50</div>
  <p class="item-desc on-dark" style="left:27px;top:937px;width:320px">Four rolled com tortilla stuffed with shredded chicken or shredded beef and deep fried with lettuce, guacamole, tomatoes and sour cream</p>

  <!-- Enchiladas -->
  <h2 class="section-title" style="left:475px;top:341px">Enchiladas</h2>
  <div class="item-name" style="left:475px;top:381px">Enchiladas Dinner</div>
  <div class="price" style="left:791px;top:384px">$8.99</div>
  <p class="item-desc" style="left:474px;top:404px;width:385px">Two beef, chicken or cheese enchiladas, served with rice and beans.</p>
  <div class="item-name" style="left:475px;top:438px">Enchiladas Poblanas</div>
  <div class="price" style="left:796px;top:439px">$10.99</div>
  <p class="item-desc" style="left:474px;top:460px;width:392px">Three shredded chicken enchiladas smothered in Mexican sauce " Mole" served with sour cream, sliced onions, shredded cheese and rice</p>
  <div class="item-name" style="left:475px;top:508px">Enchiladas de Bistec</div>
  <div class="price" style="left:796px;top:509px">$11.99</div>
  <p class="item-desc" style="left:474px;top:529px;width:385px">Three steak enchiladas covered in green sauce served with rice, beans, lettuce, guacamole and picodegallo.</p>
  <div class="item-name" style="left:475px;top:573px">Enchiladas de Bistec</div>
  <div class="price" style="left:798px;top:574px">$11.99</div>
  <p class="item-desc" style="left:474px;top:594px;width:385px">Three steak enchiladas covered in green sauce served with rice, beans, lettuce, guacamole and picodegallo.</p>
  <div class="item-name" style="left:475px;top:639px">Enchiladas Suizas</div>
  <div class="price" style="left:798px;top:640px">$11.25</div>
  <p class="item-desc" style="left:474px;top:661px;width:392px">Four chicken enchiladas covered in cheese and green sauce with mozzarella cheese on top.</p>
  <div class="item-name" style="left:475px;top:703px">Enchiladas Supreme</div>
  <div class="price" style="left:800px;top:704px">$10.95</div>
  <p class="item-desc" style="left:474px;top:725px;width:392px">One beef, one chicken, one bean and one cheese served with lettuice, tomatoes and sour cream.</p>
  <div class="item-name" style="left:475px;top:764px">Enchiladas de Camaron</div>
  <div class="price" style="left:801px;top:765px">$11.59</div>
  <p class="item-desc" style="left:474px;top:785px;width:392px">Shrimp enchiladas, three enchiladas served in green sauce. with rice beans, lettuce pico de gallo and guacamole.</p>

  <!-- Extras -->
  <section class="extras">
    <p class="extras-fee">Each extra ingredient : $1.00</p>
    <p class="extras-list">Lettuce, Chopped Tomatoes, Pico de Gallo, Sour Cream,<br>shredded cheese, guacamole, jalapenos, green sauce or cheese dip.</p>
    <p class="extras-notice">Notice: May be cooked to order. Consuming raw or under cooked meats, poultry, seafood, shelfish or<br>eggs may increase your risk of foodborne illness, especially if yopu have certain medical conditions.</p>
  </section>
</main>
</body>
</html>
```